Billboard Kernhuis - Atelier Z

I need two Billboards (125cm width x 340 height) -. They will be standing side by side in front of a building. Each billboard contains details of a business. 1. Medical center: KERNHUIS MARVELDE 2. Beauty saloon/Permanent make-up. ATELIER Z & PMU Clinic. We already have a mockup. (see uploads). We want a design fitting the building with upmarket look. Modern, fresh and classy. The billboards need to have the same background color as in the mockup: dark-grey/black. The medical center has a green accent and the Beauty salon soft pink. The billboards should have certain uniformity.

Target Market(s)

Upmarket men and women

Font styles to use
Sans Serif

Requirements
Must have
• WE LIKE OUT OF THE BOX DESIGNS

KERNHUIS MARVELDE
Uw rug is onze zorg - this is the tagline
hello@kernhuismarvelde-demo.be
09 481 26 70
www.kernhuismarvelde-demo.be
facebook icon | instagram icon

ATELIER Z (HAS TWO DEPARTMENTS)
1. Schoonheidsinstituut - (which means beauty salon)
2. Lijnwerk Clinic (which means permanent make up)
0486 51 93 40
hello@atelierz-demo.be
www.atelierz-demo.be

hello@atelierz-demo.be
Should not have
• not curly, not kitch, no color-books
NO PICTURES IN DESIGN

```html
<!DOCTYPE html>
<html lang="nl">
<head>
<meta charset="utf-8">
<title>Billboards Kernhuis Marvelde &amp; Atelier Z</title>
<link rel="stylesheet" href="https://fonts.googleapis.com/css2?family=Montserrat:wght@300;400&family=Lato:wght@700&family=Oswald:wght@300&display=swap">
<style>
  :root {
    --page: #ececec;
    --board: #363636;
    --white: #ffffff;
    --green: #8cc63f;
    --pink: #f9c9c9;
    --pink-line: #d9a9a9;
  }
  * { margin: 0; padding: 0; box-sizing: border-box; }
  html, body { width: 1200px; height: 1200px; overflow: hidden; }
  body { background: var(--page); position: relative; font-family: "Montserrat", sans-serif; }

  .billboard {
    position: absolute; top: 98px; width: 369px; height: 1004px;
    background: var(--board); overflow: hidden; color: var(--white);
  }
  .billboard--medical { left: 158px; --accent: var(--green); --rule: var(--green); }
  .billboard--beauty { left: 674px; --accent: var(--pink); --rule: var(--pink-line); }

  .waves { position: absolute; inset: 0; width: 100%; height: 100%; }

  .row {
    position: absolute; left: 0; right: 0; text-align: center;
    transform: translateY(-50%); white-space: nowrap;
  }

  /* Medical */
  .brand-name {
    font-family: "Lato", sans-serif; font-weight: 700; font-size: 26px;
    letter-spacing: 0.06em; line-height: 31px; color: var(--white);
    text-align: left; left: 51px; right: auto;
  }
  .brand-dot {
    position: absolute; left: 300px; top: 150px; width: 26px; height: 26px;
    border-radius: 50%; background: var(--green);
  }
  .tagline { font-weight: 300; font-size: 55px; line-height: 1; }
  .tagline--accent { color: var(--green); }

  /* Beauty */
  .business-name { font-weight: 300; font-size: 26px; color: var(--white); }
  .department {
    font-family: "Oswald", sans-serif; font-weight: 300; font-size: 43px;
    color: var(--pink); line-height: 1;
  }
  .clinic-sub { font-weight: 400; font-size: 9px; letter-spacing: 0.2em; }

  /* Contact block */
  .divider {
    position: absolute; left: 50%; transform: translate(-50%, -50%);
    display: flex; align-items: center; gap: 7px;
  }
  .divider::before, .divider::after { content: ""; display: block; height: 1px; background: var(--rule); }
  .billboard--medical .divider::before, .billboard--medical .divider::after { width: 109px; }
  .billboard--beauty .divider::before, .billboard--beauty .divider::after { width: 92px; }
  .divider svg { width: 18px; height: 14px; stroke: var(--rule); fill: none; stroke-width: 1.2; }

  .contact { font-weight: 300; font-size: 17px; letter-spacing: 0.01em; }
  .billboard--beauty .contact { font-size: 16px; }
  .contact .hl { color: var(--accent); }

  .social {
    position: absolute; left: 50%; transform: translate(-50%, -50%);
    display: flex; align-items: center; justify-content: center; gap: 20px;
    height: 30px; border-radius: 15px; background: var(--white);
  }
  .billboard--medical .social { width: 120px; }
  .billboard--beauty .social { width: 100px; }
  .social-dot { width: 20px; height: 20px; border-radius: 50%; background: #3b5998; }
  .social-dot--second { background: #d6336c; }
  .social-line { position: absolute; height: 1px; background: var(--rule); }
</style>
</head>
<body>

<section class="billboard billboard--medical">
  <svg class="waves" viewBox="0 0 594 1618" preserveAspectRatio="none" aria-hidden="true">
    <path fill="#8cc63f" d="M0,755 C150,850 400,880 594,815 C450,900 300,940 150,920 C80,910 30,890 0,872 Z"/>
    <path fill="#ffffff" d="M0,725 C150,835 420,890 594,810 L594,818 C420,880 150,860 0,757 Z"/>
    <path fill="#8cc63f" d="M105,1618 C200,1520 330,1480 420,1490 C500,1500 560,1530 594,1548 L594,1556 C520,1525 430,1512 360,1530 C300,1550 250,1585 210,1618 Z"/>
    <path fill="#ffffff" d="M210,1618 C270,1560 360,1520 440,1515 C500,1515 560,1535 594,1552 L594,1558 C540,1542 470,1537 410,1547 C340,1562 280,1592 240,1618 Z"/>
  </svg>

  <div class="row brand-name" style="top:226px">KERNHUIS<br>MARVELDE</div>
  <div class="brand-dot"></div>

  <div class="row tagline" style="top:348px">Uw rug is</div>
  <div class="row tagline tagline--accent" style="top:407px">onze zorg</div>

  <div class="divider" style="top:635px"><svg viewBox="0 0 18 14"><rect x="1" y="1.5" width="16" height="11"/><path d="M1 1.5 L9 8 L17 1.5 M1 12.5 L7 6.5 M17 12.5 L11 6.5"/></svg></div>
  <div class="row contact" style="top:665px">hello@kernhuismarvelde-demo.be</div>
  <div class="divider" style="top:699px"><svg viewBox="0 0 18 14"><path d="M4 2 L6.5 1.5 L7.5 4.5 L6 5.5 C7 8 8.5 9.5 10.5 10.5 L11.5 9 L14.5 10 L14 12.5 C8 13 3.5 8 4 2 Z"/><path d="M10 2 A4 4 0 0 1 14 6 M10 4 A2 2 0 0 1 12 6"/></svg></div>
  <div class="row contact" style="top:728px">09 481 26 70</div>
  <div class="divider" style="top:757px"><svg viewBox="0 0 18 14"><path d="M15 1 C11 1 8 4 6.5 8 L8.5 10 C12.5 8.5 15 5 15 1 Z"/><circle cx="11.5" cy="4.7" r="1.2"/><path d="M6.5 8 L4 8 L6 5.5 M8.5 10 L8.5 12.5 L11 10.5 M5 10 L2 13"/></svg></div>
  <div class="row contact" style="top:792px">www.<span class="hl">kernhuismarvelde-demo</span>.be</div>

  <div class="social-line" style="left:56px;width:70px;top:846px"></div>
  <div class="social-line" style="left:243px;width:70px;top:846px"></div>
  <div class="social" style="top:846px"><span class="social-dot"></span><span class="social-dot social-dot--second"></span></div>
</section>

<section class="billboard billboard--beauty">
  <svg class="waves" viewBox="0 0 594 1618" preserveAspectRatio="none" aria-hidden="true">
    <path fill="#f9c9c9" d="M0,755 C150,850 400,880 594,815 C450,900 300,940 150,920 C80,910 30,890 0,872 Z"/>
    <path fill="#ffffff" d="M0,725 C150,835 420,890 594,810 L594,818 C420,880 150,860 0,757 Z"/>
    <path fill="#f9c9c9" d="M105,1618 C200,1520 330,1480 420,1490 C500,1500 560,1530 594,1548 L594,1556 C520,1525 430,1512 360,1530 C300,1550 250,1585 210,1618 Z"/>
    <path fill="#ffffff" d="M210,1618 C270,1560 360,1520 440,1515 C500,1515 560,1535 594,1552 L594,1558 C540,1542 470,1537 410,1547 C340,1562 280,1592 240,1618 Z"/>
  </svg>

  <div class="row business-name" style="top:190px">Atelier Z</div>
  <div class="row department" style="top:253px">Schoonheidsinstituut</div>

  <div class="divider" style="top:313px"><svg viewBox="0 0 18 14"><rect x="1" y="1.5" width="16" height="11"/><path d="M1 1.5 L9 8 L17 1.5 M1 12.5 L7 6.5 M17 12.5 L11 6.5"/></svg></div>
  <div class="row contact" style="top:336px">hello@atelierz-demo.be</div>
  <div class="divider" style="top:362px"><svg viewBox="0 0 18 14"><path d="M4 2 L6.5 1.5 L7.5 4.5 L6 5.5 C7 8 8.5 9.5 10.5 10.5 L11.5 9 L14.5 10 L14 12.5 C8 13 3.5 8 4 2 Z"/><path d="M10 2 A4 4 0 0 1 14 6 M10 4 A2 2 0 0 1 12 6"/></svg></div>
  <div class="row contact" style="top:386px">0486 51 93 40</div>
  <div class="divider" style="top:407px"><svg viewBox="0 0 18 14"><path d="M15 1 C11 1 8 4 6.5 8 L8.5 10 C12.5 8.5 15 5 15 1 Z"/><circle cx="11.5" cy="4.7" r="1.2"/><path d="M6.5 8 L4 8 L6 5.5 M8.5 10 L8.5 12.5 L11 10.5 M5 10 L2 13"/></svg></div>
  <div class="row contact" style="top:435px">www.<span class="hl">atelierz-demo</span>.be</div>

  <div class="social-line" style="left:76px;width:60px;top:476px"></div>
  <div class="social-line" style="left:232px;width:60px;top:476px"></div>
  <div class="social" style="top:476px"><span class="social-dot"></span><span class="social-dot social-dot--second"></span></div>

  <div class="row business-name" style="top:634px">Lijnwerk Clinic</div>
  <div class="row clinic-sub" style="top:681px">PERMANENT MAKE UP BY LOTTE VERHAEGEN</div>
  <div class="row department" style="top:726px">Permanent Make up</div>

  <div class="divider" style="top:777px"><svg viewBox="0 0 18 14"><rect x="1" y="1.5" width="16" height="11"/><path d="M1 1.5 L9 8 L17 1.5 M1 12.5 L7 6.5 M17 12.5 L11 6.5"/></svg></div>
  <div class="row contact" style="top:800px">hello@lijnwerk-demo.be</div>
  <div class="divider" style="top:826px"><svg viewBox="0 0 18 14"><path d="M4 2 L6.5 1.5 L7.5 4.5 L6 5.5 C7 8 8.5 9.5 10.5 10.5 L11.5 9 L14.5 10 L14 12.5 C8 13 3.5 8 4 2 Z"/><path d="M10 2 A4 4 0 0 1 14 6 M10 4 A2 2 0 0 1 12 6"/></svg></div>
  <div class="row contact" style="top:849px">0486 51 93 40</div>
  <div class="divider" style="top:870px"><svg viewBox="0 0 18 14"><path d="M15 1 C11 1 8 4 6.5 8 L8.5 10 C12.5 8.5 15 5 15 1 Z"/><circle cx="11.5" cy="4.7" r="1.2"/><path d="M6.5 8 L4 8 L6 5.5 M8.5 10 L8.5 12.5 L11 10.5 M5 10 L2 13"/></svg></div>
  <div class="row contact" style="top:898px">www.<span class="hl">lijnwerk-demo</span>.be</div>
</section>

</body>
</html>
```